Tarnby Group letterhead

Hi,

I need a letterhead template created for our business. This should be done in word format and A4 size. The images need to not move in the template ie when I am adding writing in etc. and should flow on when I get to a second page.

I have attached our logo templates below.

Other details to include on the letterhead somewhere are:

0438 915 267
Max@Tarnbyelectrical.example.au
PO Box 817 Marrowvale NSW 2190
ABN: 57 318 962 407

Thanks!

```html
<!DOCTYPE html>
<html lang="en">
<head>
<meta charset="utf-8">
<title>Tarnby Group Letterhead</title>
<link href="https://fonts.googleapis.com/css2?family=Roboto:wght@400;900&display=swap" rel="stylesheet">
<style>
  :root {
    --orange: #e95419;
    --crimson: #9a1a2f;
    --ink: #111111;
    --muted: #8a8a8a;
    --paper: #ffffff;
  }
  html, body { margin: 0; padding: 0; overflow: hidden; background: var(--paper); }
  .letterhead {
    position: relative;
    width: 849px;
    height: 1200px;
    overflow: hidden;
    background: var(--paper);
    font-family: "Roboto", Arial, sans-serif;
    color: var(--ink);
  }
  .frame { position: absolute; inset: 0; width: 849px; height: 1200px; }
  .brand {
    position: absolute;
    left: 25px;
    top: 66px;
    width: 264px;
    text-align: center;
  }
  .brand-mark {
    display: block;
    width: 84px;
    height: 84px;
    margin: 0 auto;
    border-radius: 50%;
    border: 6px solid #222;
    box-sizing: border-box;
  }
  .brand-name {
    margin-top: 22px;
    font-weight: 900;
    font-size: 27px;
    letter-spacing: 1px;
    color: var(--orange);
    text-transform: uppercase;
  }
  .text { position: absolute; margin: 0; font-size: 13.2px; line-height: 17.6px; white-space: nowrap; }
  .salutation { left: 15px; top: 302px; font-size: 15.5px; line-height: 22px; }
  .salutation .role { color: var(--muted); }
  .date { left: 575px; top: 302px; font-size: 15.5px; line-height: 22px; }
  .body { left: 15px; top: 404px; }
  .body p { margin: 0 0 17.6px; }
  .closing { left: 15px; top: 790px; font-size: 15.5px; line-height: 20px; }
  .signature {
    position: absolute;
    left: 20px;
    top: 830px;
    width: 205px;
    height: 68px;
    background: linear-gradient(90deg, rgba(233,84,25,0.14), rgba(233,84,25,0.04));
  }
  .signatory { left: 15px; top: 912px; font-size: 15.5px; line-height: 25.5px; }
  .contact {
    position: absolute;
    left: 588px;
    top: 1035px;
    margin: 0;
    padding: 0;
    list-style: none;
    font-size: 13.2px;
    white-space: nowrap;
  }
  .contact li { display: flex; align-items: center; height: 27px; }
  .contact .icon {
    width: 24px; height: 24px;
    border-radius: 5px;
    background: var(--orange);
    margin-right: 5px;
    display: flex; align-items: center; justify-content: center;
  }
</style>
</head>
<body>
<div class="letterhead">
  <svg class="frame" viewBox="0 0 1191 1684" preserveAspectRatio="none" aria-hidden="true">
    <defs>
      <linearGradient id="band" x1="0" x2="1" y1="0" y2="0">
        <stop offset="0" stop-color="#e95419"/>
        <stop offset="1" stop-color="#9a1a2f"/>
      </linearGradient>
    </defs>
    <rect x="0" y="0" width="438" height="60" fill="url(#band)"/>
    <path d="M438,0 H1191 V312 C1160,170 1010,90 760,90 H438 Z" fill="#e95419"/>
    <path d="M0,1370 C40,1530 230,1590 470,1593 L438,1622 V1684 H0 Z" fill="url(#band)"/>
    <path d="M438,1622 H1191 V1684 H438 Z" fill="#e95419"/>
  </svg>

  <div class="brand">
    <span class="brand-mark"></span>
    <div class="brand-name">Tarnby Group</div>
  </div>

  <div class="text salutation">Dear (Name)<br><span class="role">workstation</span></div>
  <div class="text date">Date: 17 December, 2024</div>

  <div class="text body">
    <p>Lorem ipsum dolor sit amet, consectetur adipiscing elit. Fusce eget aliquam tortor. Fusce sed ornare sem,<br>at luctus lectus. Suspendisse mattis condimentum egestas. Etiam pharetra erat mattis, tincidunt mi at,<br>lacinia ante. Aenean quis viverra diam. Maecenas pulvinar metus sed tempus molestie. Curabitur nisl massa,<br>faucibus id aliquet non, euismod malesuada leo.</p>
    <p>Etiam est ex, elementum ac cursus ac, luctus fringilla eros. Nullam tellus libero, porta maximus rhoncus et,<br>&nbsp;facilisis et nibh. Vestibulum rutrum commodo sem, non auctor tellus rhoncus id. Phasellus rhoncus faucibus urna,<br>eget condimentum velit scelerisque at. Quisque a lacus vel nisl faucibus mattis. Mauris id tempus justo.<br>Suspendisse et vulputate odio. Sed gravida, enim vitae eleifend fermentum, nulla ligula tempor elit, eu<br>suscipit urna ligula eget lorem. Proin condimentum ligula a ex laoreet laoreet. Sed vitae massa et odio facilisis<br>lobortis a eget enim. Etiam eu mi lorem. Donec dolor nulla, ultrices sit amet ultricies egestas, blandit sed purus.<br>Maecenas congue augue id velit finibus, nec suscipit sem pulvinar. Proin varius quam dictum elementum molestie.<br>Suspendisse a faucibus lacus. Ut sed maximus ex.</p>
    <p>Sed commodo mi ut enim pulvinar, at hendrerit ex interdum. Sed suscipit ex velit, ac elementum libero cursus id.<br>Maecenas at nisl dolor. Proin eu vehicula leo. Aenean dignissim vestibulum molestie. Morbi congue pharetra sem ut finibus.<br>&nbsp;Nunc nec nibh leo. Praesent rhoncus felis massa. Nulla sagittis, enim sit amet lobortis malesuada, risus massa facilisis neque,<br>sed porta turpis mi facilisis ex. Nulla hendrerit euismod mi. Ut aliquet laoreet ipsum, sodales feugiat augue dignissim a. Vivamus<br>nulla urna, euismod quis nunc a, lacinia molestie sapien.</p>
  </div>

  <div class="text closing">SINCERELY YOURS</div>
  <div class="signature" role="img" aria-label="Handwritten signature"></div>
  <div class="text signatory">NAME<br>POST TITLE</div>

  <ul class="contact">
    <li><span class="icon"><svg width="14" height="14" viewBox="0 0 24 24"><path d="M3 14c0-4 4-6 9-6s9 2 9 6l-4 1-1-3c-3-1-5-1-8 0l-1 3z" fill="#fff"/></svg></span>0438 915 267</li>
    <li><span class="icon"><svg width="15" height="12" viewBox="0 0 24 18"><rect x="2" y="2" width="20" height="14" rx="2" fill="none" stroke="#fff" stroke-width="2"/><path d="M3 3l9 7 9-7" fill="none" stroke="#fff" stroke-width="2"/></svg></span>Max@Tarnbyelectrical.example.au</li>
    <li><span class="icon"><svg width="14" height="14" viewBox="0 0 24 24"><rect x="3" y="8" width="18" height="10" rx="3" fill="#fff"/><rect x="11" y="18" width="2" height="5" fill="#fff"/><rect x="14" y="2" width="5" height="4" fill="#fff"/></svg></span>PO Box 817 Marrowvale NSW 2190</li>
    <li><span class="icon"><svg width="14" height="14" viewBox="0 0 24 24"><rect x="3" y="5" width="18" height="14" rx="2" fill="none" stroke="#fff" stroke-width="2"/><rect x="6" y="9" width="6" height="6" fill="#fff"/><path d="M14 10h5M14 14h5" stroke="#fff" stroke-width="2"/></svg></span>ABN: 57 318 962 407</li>
  </ul>
</div>
</body>
</html>
```